Steel band poster - help us recruit more teenage kids!

Lanternfall are a 20 person community steel band based at Harrowgate Academy, Tottenham, London, UK.

We need a poster to get some new recruits signed up before the summer!

Happy to follow your style, but we were thinking something contemporary like this Felix QT cover:http://tunewirefeed.example/news/58314-hear-felix-qts-latest-track/

If possible would be good to have maybe 3 pictures too: one of the band leader Marcus (see attached pictures), one of Solenne, one of Brix.

Get in touch!

Owen
Updates

Anyone out there? We really need a poster!

Target Market(s)

11-16 yr old London Kids

Industry/Entity Type

Steel

Font styles to use
Sans Serif

Requirements
Must have
• Bright colours, bold text, contemporary feel
Nice to have
• photos

```html
<!DOCTYPE html>
<html lang="en">
<head>
<meta charset="utf-8">
<title>Lanternfall Needs You – Steel Band Recruitment Poster</title>
<link rel="stylesheet" href="https://fonts.googleapis.com/css2?family=Montserrat:wght@400;600;800&family=Oswald:wght@500;700&display=swap">
<style>
  :root {
    --backdrop: #d9d9d9;
    --sun-yellow: #f4e21a;
    --mid-orange: #f6a11e;
    --hot-red: #ee3a2a;
    --band-pink: #f0306e;
    --needs-green: #3fb83a;
    --ink: #111111;
    --paper: #ffffff;
    --figure-tone: #8a5a3c;
    --figure-shadow: #3a2a22;
    --box-yellow: #f5ec2a;
    --box-red: #e8262f;
  }
  * { box-sizing: border-box; margin: 0; padding: 0; }
  html, body { width: 1200px; height: 932px; overflow: hidden; }
  body {
    background: var(--backdrop);
    font-family: "Montserrat", Arial, sans-serif;
    position: relative;
  }
  .poster {
    position: absolute;
    left: 310px; top: 26px;
    width: 580px; height: 880px;
    background: linear-gradient(180deg, var(--sun-yellow) 0%, var(--mid-orange) 48%, var(--hot-red) 100%);
    overflow: hidden;
    color: var(--ink);
  }
  .poster__strapline {
    position: absolute; left: 60px; top: 22px;
    width: 300px;
    font-size: 11px; line-height: 14px; font-weight: 600;
  }
  .name-band {
    position: absolute; left: 58px; top: 62px;
    width: 330px; height: 66px;
    background: var(--band-pink);
    transform: rotate(-5deg);
    display: flex; align-items: center; justify-content: center;
  }
  .name-band__text {
    font-family: "Oswald", Arial, sans-serif;
    font-weight: 700; font-size: 46px; letter-spacing: 1px;
    color: var(--ink);
  }
  .needs {
    position: absolute; left: 398px; top: 70px;
    font-family: "Oswald", Arial, sans-serif;
    font-weight: 500; font-size: 32px;
  }
  .figure {
    position: absolute; left: 150px; top: 230px;
    width: 230px; height: 450px;
    border-radius: 90px 90px 20px 20px;
    background: linear-gradient(180deg, var(--figure-tone) 0%, var(--figure-tone) 55%, var(--figure-shadow) 100%);
  }
  .letter-block {
    position: absolute; top: 215px;
    height: 135px;
    background: var(--needs-green);
    font-family: "Oswald", Arial, sans-serif;
    font-weight: 700; font-size: 150px; line-height: 135px;
    text-align: center;
  }
  .letter-block--y { left: 105px; width: 110px; }
  .letter-block--u { left: 330px; width: 110px; }
  .wanted-sign {
    position: absolute; left: 80px; top: 420px;
    width: 360px; height: 170px;
    background: var(--paper);
    transform: rotate(12deg);
    padding: 14px 22px;
  }
  .wanted-sign__title {
    font-family: "Oswald", Arial, sans-serif;
    font-weight: 700; font-size: 58px; line-height: 60px;
  }
  .wanted-sign__detail {
    font-size: 11px; line-height: 14px; font-weight: 600; margin-top: 6px;
  }
  .contact-rail {
    position: absolute; left: 22px; top: 590px;
    transform: rotate(-90deg); transform-origin: left top;
    white-space: nowrap;
    font-size: 17px; font-weight: 600; letter-spacing: 1px;
  }
  .info-box {
    position: absolute; top: 685px; height: 175px;
    padding: 16px;
    font-size: 11px; line-height: 15px; font-weight: 600;
  }
  .info-box--venue { left: 20px; width: 225px; background: var(--box-yellow); }
  .info-box--venue p + p { margin-top: 12px; }
  .info-box--details { left: 245px; width: 315px; background: var(--box-red); color: var(--box-yellow); }
  .info-box--details p + p { margin-top: 12px; }
  .corner-square {
    position: absolute; left: 205px; top: 685px;
    width: 40px; height: 30px; background: var(--needs-green);
  }
</style>
</head>
<body>
  <main class="poster">
    <p class="poster__strapline">Steel pan band is looking for new players aged 11 to 16, come along and join in</p>

    <div class="name-band"><span class="name-band__text">LANTERNFALL</span></div>
    <span class="needs">NEEDS</span>

    <div class="figure" role="img" aria-label="Photo of band leader Marcus holding a steel pan"></div>

    <div class="letter-block letter-block--y">Y</div>
    <div class="letter-block letter-block--u">U</div>

    <div class="wanted-sign">
      <div class="wanted-sign__title">Wanted</div>
      <p class="wanted-sign__detail">Young players to join our community steel band, no experience needed, every week this summer</p>
    </div>

    <div class="contact-rail">07700 900 482 &nbsp; marcus@lanternfallpan.co.uk</div>

    <section class="info-box info-box--venue">
      <p>Harrowgate Academy<br>Woodside Road<br>Tottenham<br>London</p>
      <p>Every Monday</p>
      <p>From 5.30pm to 7.30pm</p>
    </section>
    <div class="corner-square"></div>

    <section class="info-box info-box--details">
      <p>Learn to play steel pan with a friendly band of twenty players</p>
      <p>Free sessions for all ages 11 to 16, just turn up</p>
      <p>Perform at local carnivals and summer shows</p>
    </section>
  </main>
</body>
</html>
```